Letterhead and Envelope Design for Investment Company

We need a letterhead and envelope design.
We are a family owned investment company doing direct investments into other family owned businesses.
I have attached all our current marketing material including our logo for reference.

Our under construction website can be found here:
https://owen-darby-qk7m.sitebrella.example/
password: Marrowdale

Target Market(s)

Bankers, business owners, financial partners

Industry/Entity Type

Investment

Colors

Designer to choose colors to be used in the design.

Requirements
Must have
• Logo, and company information

```html
<!DOCTYPE html>
<html lang="en">
<head>
<meta charset="utf-8">
<title>Marrowdale Holdings Stationery</title>
<link href="https://fonts.googleapis.com/css2?family=Cinzel:wght@500&family=PT+Sans&family=Arimo&display=swap" rel="stylesheet">
<style>
  :root {
    --ink: #15181a;
    --gold: #e1b12c;
    --gold-text: #d9a01c;
    --paper: #f5f4f2;
    --body: #4a4a4a;
    --backdrop: #e4e2df;
    --white: #ffffff;
  }
  * { box-sizing: border-box; margin: 0; padding: 0; }
  html, body { width: 1200px; height: 791px; overflow: hidden; background: var(--backdrop); }
  .canvas { position: relative; width: 1200px; height: 791px; }

  .letterhead {
    position: absolute; left: 38px; top: 34px; width: 512px; height: 723px;
    background: var(--paper); box-shadow: 0 1px 4px rgba(0,0,0,.25);
    font-family: "PT Sans", sans-serif; color: var(--body);
  }
  .band { position: absolute; left: 0; top: 0; display: block; }
  .brand-name {
    position: absolute; left: 0; right: 0; text-align: center;
    font-family: "Cinzel", serif; font-weight: 500; color: var(--white);
    letter-spacing: .5px;
  }
  .letterhead .brand-name { top: 58px; font-size: 14px; }

  .salutation { position: absolute; left: 46px; top: 198px; font-size: 14px; color: #555; }
  .letter-body { position: absolute; left: 46px; top: 240px; width: 424px; font-size: 7.9px; line-height: 12.6px; text-align: justify; }
  .letter-body p + p { margin-top: 12.6px; }
  .closing { position: absolute; left: 46px; top: 507px; font-size: 8px; }
  .signature { position: absolute; left: 43px; top: 528px; width: 70px; height: 28px; background: linear-gradient(90deg, rgba(40,50,70,.12), rgba(40,50,70,.05)); border-radius: 3px; }
  .signer { position: absolute; left: 48px; top: 564px; font-size: 8px; line-height: 10px; }

  .footer { position: absolute; left: 0; right: 0; text-align: center; font-family: "Arimo", sans-serif; font-size: 7.4px; color: #444; }
  .letterhead .footer { top: 679px; line-height: 10.6px; }
  .gold { color: var(--gold-text); }
  .label { color: var(--gold-text); font-weight: bold; }

  .envelope {
    position: absolute; left: 577px; width: 577px; height: 262px;
    background: var(--paper); box-shadow: 0 1px 4px rgba(0,0,0,.25);
    font-family: "PT Sans", sans-serif;
  }
  .envelope-back { top: 216px; }
  .envelope-front { top: 494px; }
  .flap { position: absolute; left: 0; top: 0; display: block; }
  .envelope-back .brand-name { top: 42px; font-size: 10px; }
  .flap-url { position: absolute; left: 0; right: 0; top: 64px; text-align: center; font-size: 8px; color: var(--white); }
  .envelope-front .brand-name { left: 31px; right: auto; top: 56px; font-size: 12px; }
  .envelope-front .footer { top: 230px; }
</style>
</head>
<body>
<main class="canvas">

  <section class="letterhead">
    <svg class="band" width="512" height="128" viewBox="0 0 512 128">
      <path d="M0 0 H512 V123 Q256 67 0 123 Z" fill="var(--ink)"/>
      <path d="M0 123 Q256 67 512 123" fill="none" stroke="var(--gold)" stroke-width="2.5"/>
    </svg>
    <div class="brand-name">Marrowdale Holdings Inc</div>

    <p class="salutation">Dear Mr. Calloway,</p>
    <div class="letter-body">
      <p>Lorem ipsum dolor sit amet, consectetur adipiscing elit. Donec orci purus, luctus vitae dignissim eu, iaculis sed purus. Vivamus faucibus, ipsum nec aliquet viverra, leo mauris condimentum ligula, sit amet sagittis enim ligula quis arcu. Nam egestas tortor id nisi porttitor mattis. In tortor ante, ultricies in suscipit a, tempus non massa. Vivamus et auctor mi. Fusce vel massa nulla. Phasellus nec eros mauris, et scelerisque orci.</p>
      <p>Donec malesuada orci vitae nulla accumsan porta a id massa. Quisque accumsan iaculis magna sit amet fringilla. Maecenas consequat, magna eget tincidunt semper, odio nibh rutrum mi, id feugiat ante nisi eu risus. Vestibulum nunc orci, rhoncus a placerat in, ultricies in mi. Cras mattis varius eros, vel fringilla nisi suscipit eget. Quisque scelerisque sagittis nulla at porttitor.</p>
      <p>Sed id augue vitae urna euismod commodo aliquet a quam. Pellentesque arcu velit, cursus et malesuada ut, consequat et diam. Nullam erat sem, rhoncus id ullamcorper vitae, rhoncus et arcu. In ultricies ultricies nulla, ut rutrum nisi iaculis at. Donec eu magna a metus ornare faucibus. Fusce aliquet faucibus ultricies. Morbi semper, est id tincidunt gravida, sem arcu adipiscing lacus, ac bibendum nulla leo eu purus. Quisque nec diam sed risus consectetur a ccumsan quis quis nibh. Vestibulum id purus lorem.</p>
      <p>It is a long established fact that a reader will be distracted by the readable content of a page when looking at its layout. The point of using Lorem Ipsum is that it has a more-or-less normal distribution of letters, as opposed to using 'Content here, content here', making it look like readable English. Many desktop publishing packages</p>
    </div>
    <p class="closing">Sincerely,</p>
    <div class="signature" role="img" aria-label="Handwritten signature"></div>
    <p class="signer">Owen Darby<br>Founder</p>

    <div class="footer">
      <span class="gold">Marrowdale Holdings, Inc.,</span>418 Harbor Ave. NE; Suite 210, Fenwick, IA 50900<br>
      <span class="label">P:</span> 555-014-2287 <span class="label">E:</span> inquiries@marrowdaleholdings.example <span class="label">W:</span> www.marrowdaleholdings.example
    </div>
  </section>

  <section class="envelope envelope-back">
    <svg class="flap" width="577" height="96" viewBox="0 0 577 96">
      <path d="M0 0 H577 L563 72 Q558 95 535 95 H42 Q19 95 14 72 Z" fill="var(--ink)"/>
    </svg>
    <div class="brand-name">Marrowdale Holdings</div>
    <p class="flap-url">www.marrowdaleholdings.example</p>
  </section>

  <section class="envelope envelope-front">
    <svg class="band" width="577" height="120" viewBox="0 0 577 120">
      <path d="M0 0 H577 V117 Q288 59 0 117 Z" fill="var(--ink)"/>
      <path d="M0 117 Q288 59 577 117" fill="none" stroke="var(--gold)" stroke-width="2.5"/>
    </svg>
    <div class="brand-name">Marrowdale Holdings Inc</div>
    <div class="footer"><span class="gold">Marrowdale Holdings, Inc.</span>418 Harbor Ave. NE; Suite 210, Fenwick, IA 50900</div>
  </section>

</main>
</body>
</html>
```